Lantern Lane Town Footpath Chronicle Trek

We are launching a different kind of city historical walking tour company with a slightly darker approach using historical but real stories that have long been forgotten from living memory.
Our tour is going to contain a lot of very thoroughly researched stories ranging from 50 to 150 years past that takes the customer into the actual-real life past of the city streets.  Stories that may contains some dark undertones and stories with a twist or that seem eccentric to us now but were entirely normal back in olden times - minus the dry historical facts that most tours engage in..
Our tours are going to run both day and night and will incorporate real history / real Lantern Lane, so some of the stories will be quite serious (e.g.- there are actual murders from 100 years ago, baffling court cases, even a bit of poetry written by murderers, suicides, love triangles, you name it.  We are aiming for a mystery/history theme and are aiming to attract tourists who are interested in getting a different kind of history.

We're not going for scares and even though we expect people to enjoy our tours;  we're not aiming at light fun and frivolity.  I guess if you wanted to give us a tv rating we'd be aiming at M to MA15+.
If I was to give you another analogy using the literature world.  Think Edwin Harrowgates Nocturno rather than the Moonrise Saga of movies.  Or Clara Wendham's Gravemoor rather than the Pickwells.  Even Crown of Embers rather than a soap opera.
Our stories are being carefully crafted and are packed with unexpected twists, turns & revelations whilst remaining all 100% true.  We have approx 15-20 stories for each tour and we're designing them in a way that each story will trigger a different range of emotions in the listeners on a regular basis.  We're being very careful to keep it fresh for each story so that it will next to impossible for our guests to zone out!  I personally can't stand going on a tour where mildly interesting facts are read out.  We like deep, rich stories rather than pop entertainment.
We want the website to generate a feeling/atmosphere for our product that draws the right crowd to our tours as well as making it easy to make a booking.  Basic features to include:-
Home Page
Bookings Page
Integration with a booking system will be required here via use of plugin code.
Private Functions Page
We are hoping to integrate with a booking system via use of plugin code.  If not, then a simple form enquiry type input e.g.- name, emails, subject, contact, details, preferred date/time, etc).
About Us Page :-
Dark; a euphemism for the unknown or the forgotten.  Think dark ages, dark matter, dark energy; things where knowledge is uncertain or unknown are often termed dark.   Lantern lane brings back the hidden past, the forgotten past, the past that may not want to be remembered……but these are real stories....real stories that come from the streets around you.

Some of these stories may be tales of dark things.....some may simply be a charming reminder of days gone by…..regardless these stories are compelling reminders of the amazing times that precede us…..and the forgotten people of yesteryear finally get a chance to have their story told to a fresh audience.  Through you, the people of yesterday get to live again.  Will you like what you hear?

Contact Us page:-
•	A form input type page.
•	Include space for our phone number
•	Include space for our email address
Other Items:-
Social Media Links; we will be looking for social media icons to link to our social media pages to Chatterbook, Snapfolio, Chirplet.
Subscription; we want to also capture an input email address box for site visitors.  We will be launching a weekly Lantern Lane podcast / email newsetter; with a weekly Lantern Lane from a different place in the world and we want some way for people to subscribe.

Updates
Project Deadline Extended
Reason: A few additional photos have been uploaded.  Feel free to utilize if helpful.  Our stories range from the 1800s to 1950s in an era with beautiful old Victorian buildings.  I'm putting through the extension just to give some more time to see if this gives any more ideas and inspiration.  Thank you for all the great submissions.

Target Market(s)
Tourists that want to hear a darker version of the city they are visiting. Stories that other tour companies would not even think of covering. The real history of the events that ordinary people lived through that didn't necessarily make the history books. All stories are true; as per project description.
Industry/Entity Type
Tourism
Coding
Coded - Design and coding required
Number of Pages Required
5+ page
Colors
Designer to choose colors to be used in the design.
Look and feel

```html
<!DOCTYPE html>
<html lang="en">
<head>
<meta charset="utf-8">
<title>Lantern Lane – Town Footpath Chronicle Trek</title>
<link rel="stylesheet" href="https://fonts.googleapis.com/css2?family=Roboto+Condensed:wght@400;700&family=Open+Sans:wght@400;600&display=swap">
<style>
:root{
  --red:#e8262b;
  --dark:#232323;
  --white:#ffffff;
  --sand-1:#3a4450;
  --sand-2:#8a6a44;
  --sand-3:#c48a45;
  --sand-4:#6b4a2a;
  --social-1:#3b5998;
  --social-2:#c8473b;
  --social-3:#3fa9e8;
}
*{margin:0;padding:0;box-sizing:border-box}
html,body{width:1200px;height:1026px;overflow:hidden;background:var(--dark)}
body{position:relative;font-family:"Open Sans",sans-serif;color:var(--white)}
.hero{position:absolute;left:0;top:0;width:1200px;height:680px;
  background:linear-gradient(100deg,var(--sand-4) 0%,var(--sand-2) 20%,var(--sand-1) 40%,var(--sand-2) 58%,var(--sand-3) 78%,var(--sand-4) 100%);}
.hero::after{content:"";position:absolute;inset:0;background:linear-gradient(180deg,rgba(0,0,0,.25),rgba(0,0,0,0) 40%,rgba(0,0,0,.2))}
.brand{position:absolute;left:98px;top:88px;display:flex;align-items:center;gap:10px;z-index:2;text-decoration:none;
  font-family:"Roboto Condensed",sans-serif;font-weight:700;font-size:27px;letter-spacing:1px;color:var(--white)}
.brand-dot{width:14px;height:14px;border-radius:50%;background:var(--red)}
.topbar{position:absolute;right:95px;top:16px;display:flex;align-items:center;gap:12px;z-index:2}
.call{display:flex;align-items:center;gap:10px;font-family:"Roboto Condensed",sans-serif;font-size:22px;margin-right:12px}
.social{width:34px;height:34px;border-radius:50%;display:block}
.social.chatterbook{background:var(--social-1)}
.social.snapfolio{background:var(--social-2)}
.social.chirplet{background:var(--social-3)}
.nav{position:absolute;right:98px;top:67px;display:flex;gap:22px;z-index:2;list-style:none}
.nav a{color:var(--white);text-decoration:none;font-family:"Roboto Condensed",sans-serif;font-size:18.5px;text-transform:uppercase}
.headline{position:absolute;left:0;width:1200px;top:338px;text-align:center;z-index:2;
  font-family:"Roboto Condensed",sans-serif;font-weight:700;font-size:46px;text-shadow:0 2px 6px rgba(0,0,0,.6)}
.book-btn{position:absolute;left:532px;top:412px;width:137px;height:38px;z-index:2;background:var(--red);
  border:1px solid rgba(255,255,255,.7);border-radius:5px;color:var(--white);text-align:center;line-height:36px;
  font-family:"Roboto Condensed",sans-serif;font-weight:700;font-size:21px;text-decoration:none}
.arrow{position:absolute;top:350px;width:35px;height:35px;z-index:2}
.arrow.prev{left:62px}.arrow.next{left:1101px}
.rating{position:absolute;left:1011px;top:519px;z-index:2}
.swoosh{position:absolute;left:0;top:575px;width:1200px;height:110px;z-index:3}
.footer-main{position:absolute;left:0;top:684px;width:1200px;height:240px;z-index:4}
.col-title{font-family:"Roboto Condensed",sans-serif;font-size:20px;font-weight:400;text-transform:uppercase;position:absolute;top:-8px;white-space:nowrap;line-height:24px}
.contact{position:absolute;left:101px;top:0;width:320px}
.contact-item{position:absolute;left:0;display:flex;gap:10px;font-size:14.5px;line-height:23px;white-space:nowrap}
.contact-item svg{flex:none;margin-top:4px}
.links{position:absolute;left:443px;top:0}
.links ul{list-style:none;position:absolute;top:33px;white-space:nowrap}
.links li{font-size:13px;height:25.7px;display:flex;align-items:center;gap:14px}
.links li::before{content:"";border-left:5px solid var(--white);border-top:4px solid transparent;border-bottom:4px solid transparent}
.signup{position:absolute;left:682px;top:-3px;width:340px}
.signup .col-title{top:-9px}
.signup p{position:absolute;top:28px;font-size:11.5px;line-height:19px;white-space:nowrap}
.signup input{position:absolute;top:80px;left:0;width:334px;height:41px;border:0;padding:0 14px;font:11px "Open Sans",sans-serif;color:#555}
.signup button{position:absolute;top:136px;left:0;width:98px;height:41px;border:0;background:var(--red);color:var(--white);
  font:13px "Open Sans",sans-serif;text-transform:uppercase}
.footer-band{position:absolute;left:0;top:880px;width:1200px;height:146px}
.footer-brand{position:absolute;left:0;width:1200px;top:954px;text-align:center;font-family:"Roboto Condensed",sans-serif;font-weight:700;font-size:22px;letter-spacing:1px}
.copyright{position:absolute;left:0;width:1200px;top:993px;text-align:center;font-family:Arial,sans-serif;font-size:12px}
</style>
</head>
<body>
<div class="hero" role="img" aria-label="Photograph of ornate carved sandstone palace pavilions overlooking a green hillside at dusk"></div>

<a class="brand" href="#"><span class="brand-dot"></span>LANTERN LANE</a>

<div class="topbar">
  <span class="call">
    <svg width="22" height="22" viewBox="0 0 24 24"><path fill="#fff" d="M6.6 10.8a15 15 0 006.6 6.6l2.2-2.2c.3-.3.7-.4 1-.2 1.1.4 2.3.6 3.6.6.6 0 1 .4 1 1V20c0 .6-.4 1-1 1A17 17 0 013 4c0-.6.4-1 1-1h3.5c.6 0 1 .4 1 1 0 1.3.2 2.5.6 3.6.1.3 0 .7-.2 1z"/></svg>
    Call us : 0790 5551234
  </span>
  <a class="social chatterbook" href="#" aria-label="Chatterbook"></a>
  <a class="social snapfolio" href="#" aria-label="Snapfolio"></a>
  <a class="social chirplet" href="#" aria-label="Chirplet"></a>
</div>

<ul class="nav">
  <li><a href="#">Home</a></li>
  <li><a href="#">Bookings</a></li>
  <li><a href="#">Private Functions</a></li>
  <li><a href="#">About Us</a></li>
  <li><a href="#">Get in Touch</a></li>
</ul>

<h1 class="headline">REDISCOVER FORGOTTEN HISTORY</h1>
<a class="book-btn" href="#">BOOK NOW</a>

<svg class="arrow prev" viewBox="0 0 35 35" aria-label="Previous slide"><circle cx="17.5" cy="17.5" r="17" fill="rgba(0,0,0,.55)" stroke="rgba(255,255,255,.4)"/><path d="M20 10l-7 7.5 7 7.5" fill="none" stroke="#fff" stroke-width="2.5"/></svg>
<svg class="arrow next" viewBox="0 0 35 35" aria-label="Next slide"><circle cx="17.5" cy="17.5" r="17" fill="rgba(0,0,0,.55)" stroke="rgba(255,255,255,.4)"/><path d="M15 10l7 7.5-7 7.5" fill="none" stroke="#fff" stroke-width="2.5"/></svg>

<svg class="rating" width="86" height="66" viewBox="0 0 86 66" role="img" aria-label="Content rating badge"><polygon points="20,2 66,2 84,33 66,64 20,64 2,33" fill="none" stroke="#fff" stroke-width="3"/></svg>

<svg class="swoosh" viewBox="0 0 1200 110" preserveAspectRatio="none">
  <path d="M0 75 Q600 -58 1200 75 L1200 110 L0 110 Z" fill="var(--dark)"/>
  <path d="M0 75 Q600 -58 1200 75" fill="none" stroke="#fff" stroke-width="3"/>
  <path d="M0 105 Q600 -55 1200 105" fill="none" stroke="var(--red)" stroke-width="4"/>
</svg>

<footer>
  <div class="footer-main">
    <section class="contact">
      <h2 class="col-title">Contact Us</h2>
      <div class="contact-item" style="top:38px">
        <svg width="14" height="16" viewBox="0 0 14 18"><path fill="#fff" d="M7 0a6 6 0 00-6 6c0 4.5 6 12 6 12s6-7.5 6-12a6 6 0 00-6-6zm0 8.5A2.5 2.5 0 117 3.5a2.5 2.5 0 010 5z"/></svg>
        <span>48 Old Market Street<br>Harrowford, ST 04211</span>
      </div>
      <div class="contact-item" style="top:98px">
        <svg width="14" height="14" viewBox="0 0 24 24"><path fill="#fff" d="M6.6 10.8a15 15 0 006.6 6.6l2.2-2.2c.3-.3.7-.4 1-.2 1.1.4 2.3.6 3.6.6.6 0 1 .4 1 1V20c0 .6-.4 1-1 1A17 17 0 013 4c0-.6.4-1 1-1h3.5c.6 0 1 .4 1 1 0 1.3.2 2.5.6 3.6.1.3 0 .7-.2 1z"/></svg>
        <span>Phone: 555-014-2290</span>
      </div>
      <div class="contact-item" style="top:133px">
        <svg width="16" height="14" viewBox="0 0 16 13"><rect x="1" y="1" width="14" height="11" fill="none" stroke="#fff" stroke-width="1.6"/><path d="M1 1l7 6 7-6" fill="none" stroke="#fff" stroke-width="1.6"/></svg>
        <span>Email: info@lanternlane.example</span>
      </div>
    </section>

    <nav class="links">
      <h2 class="col-title">Quick Links</h2>
      <ul>
        <li>Home</li>
        <li>Bookings</li>
        <li>Private Functions</li>
        <li>About us</li>
        <li>Contact us</li>
      </ul>
    </nav>

    <section class="signup">
      <h2 class="col-title">Bonus Lantern Lane</h2>
      <p>Sign Up to receive our weekly Lantern Lane; an old forgotten<br>100% true tale produced in audio format</p>
      <input type="text" placeholder="Enter Name">
      <button type="button">Subscribe</button>
    </section>
  </div>

  <svg class="footer-band" viewBox="0 0 1200 146" preserveAspectRatio="none">
    <path d="M0 46 L1200 40 L1200 146 L0 146 Z" fill="var(--red)"/>
    <path d="M512 46 Q595 -20 678 44 Z" fill="var(--red)"/>
  </svg>
  <div class="footer-brand">LANTERN LANE</div>
  <div class="copyright">© 2017 Lantern Lane. All Rights Reserved.</div>
</footer>
</body>
</html>
```